Business Card Design

We need a business card design that can also be aplied for postcards. We are a small indie record company that also do consulting, and development of independat artitst . I already have the name and the basic idea of what i am looking for but i am open to any suggestion.
Info for the card
Name of the company : Velmora Records
NAME : Tomas Invaldi
PHONE : 208-5536142
EMAIL : hello@velmorarecords.example
WEB: www.velmorarecords.example
Target Market(s)
Male - Female independent musicians ages 18 to 45
Industry/Entity Type
Record Company
Contact Information for Business Card
Independant records company that also works in consulting for music business models for independent artists
Look and feel
Each slider illustrates characteristics of the customer's brand and the style your logo design should communicate.

```html
<!DOCTYPE html>
<html lang="en">
<head>
<meta charset="utf-8">
<title>Velmora Records – Business Card</title>
<link rel="stylesheet" href="https://fonts.googleapis.com/css2?family=PT+Serif:wght@400;700&family=Arimo:wght@400&display=swap">
<style>
  :root {
    --page: #ffffff;
    --card-navy: #054b80;
    --ink-light: #ffffff;
    --accent-blue: #0a9ee0;
    --accent-sky: #4ab8ea;
    --accent-magenta: #c8388a;
  }
  html, body {
    margin: 0;
    padding: 0;
    width: 841px;
    height: 1200px;
    overflow: hidden;
    background: var(--page);
  }
  .sheet {
    position: relative;
    width: 841px;
    height: 1200px;
  }
  .card {
    position: absolute;
    left: 237px;
    width: 392px;
    height: 227px;
    background: var(--card-navy);
    color: var(--ink-light);
    overflow: hidden;
  }
  .card--front { top: 305px; }
  .card--back  { top: 581px; }

  .accent-panel {
    position: absolute;
    left: 12px;
    top: 12px;
    width: 106px;
    height: 202px;
    background: linear-gradient(160deg, var(--accent-blue) 0%, var(--accent-sky) 50%, var(--accent-magenta) 100%);
    opacity: 0.9;
  }

  .wordmark {
    position: absolute;
    font-family: "PT Serif", Georgia, serif;
    font-weight: 700;
    color: var(--ink-light);
    line-height: 0.95;
    text-align: center;
    margin: 0;
  }
  .wordmark--large {
    left: 124px;
    top: 66px;
    width: 170px;
    font-size: 33px;
  }
  .wordmark--small {
    left: 17px;
    top: 22px;
    width: 64px;
    font-size: 12px;
  }

  .contact {
    position: absolute;
    left: 0;
    right: 0;
    top: 90px;
    text-align: center;
  }
  .contact__name {
    font-family: "PT Serif", Georgia, serif;
    font-weight: 400;
    font-size: 21px;
    line-height: 1;
    margin: 0 0 3px;
  }
  .contact__email {
    font-family: "Arimo", Arial, sans-serif;
    font-size: 9px;
    line-height: 1.2;
    margin: 0;
  }
  .contact__phone {
    font-family: "Arimo", Arial, sans-serif;
    font-size: 13px;
    line-height: 1.3;
    margin: 0;
  }
  .web {
    position: absolute;
    left: 0;
    right: 0;
    top: 200px;
    text-align: center;
    font-family: "Arimo", Arial, sans-serif;
    font-size: 9px;
    margin: 0;
  }
</style>
</head>
<body>
<main class="sheet">
  <section class="card card--front" aria-label="Card front">
    <div class="accent-panel" role="img" aria-label="Abstract graphic of overlapping translucent blue and magenta light beams"></div>
    <p class="wordmark wordmark--large">Velmora<br>Records</p>
  </section>

  <section class="card card--back" aria-label="Card back">
    <p class="wordmark wordmark--small">Velmora<br>Records</p>
    <div class="contact">
      <p class="contact__name">Tomas Invaldi</p>
      <p class="contact__email">hello@velmorarecords.example</p>
      <p class="contact__phone">208-5536142</p>
    </div>
    <p class="web">www.velmorarecords.example</p>
  </section>
</main>
</body>
</html>
```